Effectively Manage Muscular Pain /with Remedial Massage

A flyer to sell remedial massage Therapy for muscular pain .

$10 Discount with this flyer

Use colors orange and Blak with the color of the logo provided and preferably the fonts as well .

Little spin about remedial massage:

Remedial massage is a deep massage , to create the conditions for the body’s return to normal health after injury or with muscular-skeletal disorders. It is used to treat chronic muscular-skeletal imbalances, strains, sprains, broken bones, bruising or any injury. Deep tissue massage removes blockages, damaged cells, scar tissue and adhesions [speeds up recovery Remedial massage is also used for conditions created by lifestyle for example Repetitive strain injury and Back pain.

Target Market(s)

young professionals with kids , modern suburban couples

Industry/Entity Type

Massage

Requirements
Must have
• doble sided.

Address 418 kelvinhurst Rd , Footscray Book Now 94620387

```html
<!DOCTYPE html>
<html lang="en">
<head>
<meta charset="utf-8">
<title>Kelvara Remedial Massage Flyer</title>
<link rel="stylesheet" href="https://fonts.googleapis.com/css2?family=Roboto+Condensed:wght@400;700&family=Noto+Serif:wght@400;700&display=swap">
<style>
  :root {
    --ink: #2e2b2b;
    --ink-deep: #242121;
    --orange: #f26f21;
    --paper: #ffffff;
    --text-light: #e9e6e3;
    --text-muted: #bdb8b4;
    --alert: #d71f1f;
    --stage: #d9d9d9;
  }
  * { box-sizing: border-box; margin: 0; padding: 0; }
  html, body { width: 1200px; height: 900px; overflow: hidden; }
  body {
    background: var(--stage);
    font-family: "Noto Serif", Georgia, serif;
    display: flex;
    justify-content: center;
    align-items: center;
    gap: 90px;
  }
  .flyer {
    width: 370px;
    height: 790px;
    background: var(--ink);
    display: flex;
    flex-direction: column;
    box-shadow: 0 10px 28px rgba(0,0,0,0.28);
  }
  .flyer-header {
    height: 128px;
    background: var(--ink-deep);
    display: flex;
    align-items: center;
    gap: 22px;
    padding: 0 26px;
    border-bottom: 3px solid var(--orange);
  }
  .brand-name {
    font-family: "Roboto Condensed", Arial, sans-serif;
    font-weight: 700;
    font-size: 24px;
    line-height: 1;
    color: var(--orange);
    flex: none;
  }
  .tagline {
    font-family: "Roboto Condensed", Arial, sans-serif;
    font-size: 20px;
    line-height: 1.05;
    color: var(--text-light);
    text-transform: uppercase;
    letter-spacing: 0.3px;
  }
  .photo { border-bottom: 3px solid var(--orange); }
  .photo-back-pain {
    height: 270px;
    background: radial-gradient(ellipse at 45% 65%, #e8b4b0 0%, #d8d4d2 22%, #bdbab8 55%, #f2f2f2 100%);
  }
  .photo-neck-pain {
    height: 220px;
    background: linear-gradient(160deg, #f4f4f4 0%, #e2d3c2 40%, #a9bfe0 70%, #f4f4f4 100%);
  }
  .front-body {
    flex: 1;
    padding: 22px 26px 24px;
    display: flex;
    flex-direction: column;
  }
  .intro {
    font-size: 13.6px;
    line-height: 1.55;
    color: var(--text-light);
  }
  .intro em { font-style: normal; color: var(--orange); }
  .front-footer {
    margin-top: auto;
    display: flex;
    flex-direction: column;
    gap: 14px;
  }
  .front-footer .brand-name { align-self: flex-end; }
  .call {
    display: flex;
    align-items: baseline;
    justify-content: space-between;
  }
  .call-label {
    font-weight: 700;
    font-size: 18px;
    color: var(--text-muted);
  }
  .call-number {
    font-weight: 700;
    font-size: 26px;
    color: var(--text-light);
  }
  .back-body {
    flex: 1;
    padding: 26px 22px 24px;
    display: flex;
    flex-direction: column;
  }
  .book {
    background: var(--orange);
    border: 3px solid var(--paper);
    border-radius: 14px;
    padding: 14px 10px 30px;
    text-align: center;
    color: var(--paper);
    font-weight: 700;
  }
  .book-label { font-size: 32px; line-height: 1.1; }
  .book-number { font-size: 44px; line-height: 1.1; letter-spacing: 1px; }
  .offer {
    display: flex;
    flex-direction: column;
    align-items: flex-end;
    margin-top: -26px;
    margin-right: -6px;
    gap: 16px;
  }
  .coupon {
    width: 170px;
    background: var(--paper);
    border: 2px dashed #555;
    outline: 4px solid var(--paper);
    padding: 10px;
    display: flex;
    align-items: center;
    gap: 6px;
    box-shadow: 0 4px 10px rgba(0,0,0,0.35);
  }
  .coupon-amount {
    font-family: "Roboto Condensed", Arial, sans-serif;
    font-weight: 700;
    font-size: 40px;
    color: var(--ink-deep);
    line-height: 1;
  }
  .coupon-text { display: flex; flex-direction: column; line-height: 1.1; }
  .coupon-discount {
    font-family: "Roboto Condensed", Arial, sans-serif;
    font-weight: 700;
    font-size: 17px;
    color: var(--alert);
  }
  .coupon-note { font-size: 11px; color: var(--ink-deep); }
  .address {
    width: 170px;
    font-size: 14px;
    line-height: 1.45;
    color: var(--text-light);
  }
  .back-footer {
    margin-top: auto;
    display: flex;
    align-items: center;
    gap: 22px;
  }
</style>
</head>
<body>

  <section class="flyer flyer-front">
    <header class="flyer-header">
      <span class="brand-name">Kelvara</span>
      <p class="tagline">Osteopathy<br>Clinical Pilates</p>
    </header>
    <div class="photo photo-back-pain" role="img" aria-label="Photo of a woman holding her lower back, the painful area glowing red"></div>
    <div class="front-body">
      <p class="intro"><em>Remedial massage</em> is a deep massage, to create the conditions for the body's return to normal health after injury or with muscular-skeletal disorders. It is used to treat chronic muscular-skeletal imbalances, strains, sprains, broken bones, bruising or any injury. Deep tissue massage removes blockages, damaged cells, scar tissue and adhesions speeds up recovery. <em>Remedial massage</em> is also used for conditions created by lifestyle for example Repetitive strain injury and Back pain</p>
      <div class="front-footer">
        <span class="brand-name">Kelvara</span>
        <div class="call">
          <span class="call-label">Call Us Today</span>
          <span class="call-number">94620387</span>
        </div>
      </div>
    </div>
  </section>

  <section class="flyer flyer-back">
    <header class="flyer-header">
      <span class="brand-name">Kelvara</span>
      <p class="tagline">Osteopathy<br>Clinical Pilates</p>
    </header>
    <div class="photo photo-neck-pain" role="img" aria-label="Photo of a woman at a desk rubbing her sore neck"></div>
    <div class="back-body">
      <div class="book">
        <div class="book-label">Book Now</div>
        <div class="book-number">94620387</div>
      </div>
      <div class="offer">
        <div class="coupon">
          <span class="coupon-amount">$10</span>
          <span class="coupon-text">
            <span class="coupon-discount">DISCOUNT</span>
            <span class="coupon-note">with this flyer</span>
          </span>
        </div>
        <p class="address">418 kelvinhurst Rd,<br>Footscray</p>
      </div>
      <footer class="back-footer">
        <span class="brand-name">Kelvara</span>
        <p class="tagline">Osteopathy<br>Clinical Pilates</p>
      </footer>
    </div>
  </section>

</body>
</html>
```